Bright Harbour Electrical Limited needs advertisement brochure

We require a brochure with details of the services we provide. We have just become the only approved installer for RVL products on the Isle of Man and want to feature their producst heavily in the brochure centre pages. We estimate it will be 8 pages of A5 and we would like it to be landscape please. We have all the required content as per the word doc attached and just need it to be made to look professional. It doesn't need to include all the attached pictures and only certain information from the RVL brochure needs to be included (i.e the first couple of pages of write up).
Front Page - Just the Bright Harbour main logo and pics of vans
Page 2 - About us and the logos for who we are approved by (Kelby Traders Guild etc)
Page 3 - Domestic Electrical Services as per the word doc attached (those pictures don't have to be used so if you find better ones please go ahead and use).
Page 4 & 5 (Centre Pages) RVL information. Please make it clear that we are the only approved installers of their products on the Isle of Man.
Page 6 & 7 - Commercial Services as per the word doc attached (again if you can find better pictures than the ones contained in the word doc then feel free to use).
Page 8 - Back page to contain all our contact information.

Target Market(s)

Domestic and commercial customers. A design install and maintain company. Facility maintenance, preventative maintenance, fire alarm and emergency lighting contracts, home automation and sound system. Project management.

Industry/Entity Type

Electrical

Requirements
Must have
• Must be professional and appeal to both domestic and commercial customers. Has to be "BRIGHT" "EARTHY GREEN GLOBAL FEEL" like our logo shows. "CREATIVE" design. Possible similarity to our letter headed paper with part of the green globe down one side of the brochure. Must use Carlos Sanz text which is the Varnel Quist text same as logo. Snazzy looking, eye catching, appealing. Everything you would want to get new business in the door.
Nice to have
• As above
Should not have
• Over the top tacky earthy look. After all we also wire houses that are run by horrible oil boilers (no option). Don't want to put all my egg in one basket kind of thing.

```html
<!DOCTYPE html>
<html lang="en">
<head>
<meta charset="utf-8">
<title>Bright Harbour Electrical Limited – Brochure Pages</title>
<link href="https://fonts.googleapis.com/css2?family=Montserrat:wght@300;400;500;700&family=Lato:wght@400;700&display=swap" rel="stylesheet">
<style>
:root{
  --canvas:#ececec;
  --page:#ffffff;
  --green:#23a12e;
  --green-dark:#0a6a15;
  --green-bright:#36c43f;
  --ink:#1d1d1d;
  --grey-text:#555;
  --body-text:#6a6a6a;
  --shadow:0 2px 7px rgba(0,0,0,.35);
}
*{margin:0;padding:0;box-sizing:border-box}
html,body{width:1200px;height:981px;overflow:hidden}
body{background:radial-gradient(ellipse at 50% 40%,#fafafa 0%,var(--canvas) 75%);position:relative;font-family:"Lato",sans-serif;color:var(--ink)}
.page{position:absolute;background:var(--page);box-shadow:var(--shadow);overflow:hidden}
.bokeh{background:
  radial-gradient(circle at 12% 22%,rgba(255,255,255,.95) 0 3%,transparent 7%),
  radial-gradient(circle at 30% 48%,rgba(255,255,255,.9) 0 2%,transparent 6%),
  radial-gradient(circle at 72% 18%,rgba(255,255,255,.95) 0 4%,transparent 9%),
  radial-gradient(circle at 88% 42%,rgba(255,255,255,.9) 0 3%,transparent 7%),
  radial-gradient(circle at 55% 60%,rgba(255,255,255,.85) 0 2%,transparent 6%),
  linear-gradient(180deg,#dcdcdc 0%,#ececec 45%,#f7f7f7 70%,#fff 82%)}
.swoosh{position:absolute;left:0;bottom:0;width:100%;height:40px}
.label{position:absolute;top:314px;font-family:"Montserrat",sans-serif;font-weight:400;font-size:36px;color:var(--green-bright);letter-spacing:1px;transform:translateX(-50%)}
.brand{position:absolute;left:50%;transform:translateX(-50%);text-align:center;font-family:"Montserrat",sans-serif}
.brand-mark{display:block;margin:0 auto;border-radius:50%;background:var(--green)}
.brand-name{display:block;font-weight:700;font-size:8px;color:var(--ink);letter-spacing:.2px;margin-top:3px;white-space:nowrap}
.brand-sub{display:block;font-size:4px;color:var(--grey-text)}
.photo{position:absolute;border-radius:1px}
.h-green{position:absolute;font-family:"Montserrat",sans-serif;font-weight:400;color:var(--green)}
.copy{position:absolute;font-size:4.6px;line-height:6.2px;color:var(--body-text);text-align:justify}
.web{position:absolute;left:0;width:100%;text-align:center;font-family:"Montserrat",sans-serif;font-weight:500;color:#fff;font-size:7px}
.green-band{position:absolute;left:0;top:0;width:100%;background:linear-gradient(180deg,var(--green-bright),var(--green) 55%,var(--green-dark))}
.band-title{position:absolute;left:0;width:100%;text-align:center;color:#fff;font-family:"Montserrat",sans-serif;font-weight:400}
.band-copy{color:#eef8ee;font-size:4.4px;line-height:6px}
</style>
</head>
<body>
<svg width="0" height="0" style="position:absolute" aria-hidden="true">
  <defs>
    <linearGradient id="swooshGreen" x1="0" y1="0" x2="0" y2="1">
      <stop offset="0" stop-color="#3bcc44"/>
      <stop offset=".6" stop-color="#1b9a26"/>
      <stop offset="1" stop-color="#075e12"/>
    </linearGradient>
  </defs>
</svg>

<!-- Back cover -->
<section class="page bokeh back-cover" style="left:197px;top:47px;width:341px;height:244px">
  <div class="brand" style="top:36px">
    <span class="brand-mark" style="width:32px;height:32px"></span>
    <span class="brand-name">BRIGHT HARBOUR</span>
    <span class="brand-sub">Electrical Limited</span>
  </div>
  <p style="position:absolute;left:109px;top:101px;font-size:8.4px;line-height:11px;font-weight:700;color:#111">To discuss any of your electrical requirements<br>PLEASE CONTACT US</p>
  <div style="position:absolute;left:109px;top:131px;display:flex;align-items:center;gap:6px;color:var(--green);font-weight:700;font-size:10px">
    <svg width="9" height="9" viewBox="0 0 10 10"><circle cx="5" cy="5" r="4.5" fill="none" stroke="#222" stroke-width=".9"/><path d="M3.2 2.6l1 1-.6.8c.4.8 1 1.4 1.8 1.8l.8-.6 1 1-.8.9C4.6 7.2 2.8 5.4 2.3 3.4z" fill="#222"/></svg>
    07700 900418
  </div>
  <div style="position:absolute;left:109px;top:148px;display:flex;align-items:center;gap:6px;color:var(--green);font-weight:700;font-size:8.4px">
    <svg width="9" height="9" viewBox="0 0 10 10"><circle cx="5" cy="5" r="4.5" fill="none" stroke="#222" stroke-width=".9"/><rect x="2.6" y="3.3" width="4.8" height="3.4" fill="none" stroke="#222" stroke-width=".8"/><path d="M2.6 3.3L5 5.2l2.4-1.9" fill="none" stroke="#222" stroke-width=".7"/></svg>
    info@brightharbourelectrical.com
  </div>
  <svg class="swoosh" viewBox="0 0 340 40" preserveAspectRatio="none"><path d="M60 40C140 12 230 12 300 40Z" fill="url(#swooshGreen)"/><path d="M20 40C110 16 200 24 250 34" fill="none" stroke="#7fd985" stroke-width="1"/></svg>
  <div class="web" style="bottom:11px;font-size:7.5px">www.rvl-uk.com</div>
</section>
<div class="label" style="left:367px">BACK</div>

<!-- Front cover -->
<section class="page bokeh front-cover" style="left:614px;top:50px;width:340px;height:242px">
  <div class="brand" style="top:10px">
    <span class="brand-mark" style="width:31px;height:31px"></span>
    <span class="brand-name">BRIGHT HARBOUR</span>
    <span class="brand-sub">Electrical Limited</span>
  </div>
  <div class="photo" role="img" aria-label="Photograph of two white company vans with green livery" style="left:78px;top:68px;width:180px;height:68px;background:linear-gradient(180deg,#e8e8e8,#c9c9c9 55%,#6b6b6b);border-radius:8px"></div>
  <div style="position:absolute;left:0;width:100%;top:150px;text-align:center;font-family:'Montserrat',sans-serif;font-weight:700;font-size:25px;color:var(--green);letter-spacing:.5px">DOMESTIC</div>
  <div style="position:absolute;left:0;width:100%;top:174px;text-align:center;font-family:'Montserrat',sans-serif;font-weight:300;font-size:20px;color:#555;letter-spacing:.3px">ELECTRICAL SERVICES</div>
  <svg class="swoosh" viewBox="0 0 340 40" preserveAspectRatio="none" style="height:44px"><path d="M0 40C80 4 260 4 340 40Z" fill="url(#swooshGreen)"/><path d="M0 22C120 -4 230 4 340 28" fill="none" stroke="#fff" stroke-width="2.5"/></svg>
  <div class="web" style="bottom:12px;letter-spacing:2px">www.rvl-uk.com</div>
</section>
<div class="label" style="left:782px">FRONT</div>

<!-- About us -->
<section class="page bokeh about-page" style="left:57px;top:411px;width:339px;height:241px">
  <div style="position:absolute;left:132px;top:0;width:75px;height:65px;background:linear-gradient(#0c1a0e,#030603)">
    <div class="brand" style="top:16px">
      <span class="brand-mark" style="width:20px;height:20px"></span>
      <span class="brand-name" style="color:#fff;font-size:5.5px">BRIGHT HARBOUR</span>
      <span class="brand-sub" style="color:#bbb;font-size:3px">Electrical Limited</span>
    </div>
  </div>
  <h2 class="h-green" style="left:0;width:100%;text-align:center;top:84px;font-size:18px">About Us</h2>
  <p class="copy" style="left:36px;top:110px;width:267px">Established by Daniel Hollis in 2011 Bright Harbour Electrical Limited offers first class electrical services across the Isle of Man. Our fully qualified, professional electricians are committed to providing outstanding customer service every time. We consult closely with our domestic, commercial, and industrial clients to provide clean, modern, energy efficient systems that meet all expectations. We specialise in data networking, security lighting, home automation systems, fire alarms, emergency lighting, maintenance and inspection services.</p>
  <div style="position:absolute;left:40px;top:168px;width:262px;display:flex;justify-content:space-between;align-items:center">
    <span style="width:38px;height:14px;background:#e2592a"></span>
    <span style="width:50px;height:12px;background:#444"></span>
    <span style="width:26px;height:14px;background:#7fae1f"></span>
    <span style="width:22px;height:16px;background:#4a6fb2"></span>
    <span style="width:40px;height:10px;background:#8fcbe0"></span>
  </div>
  <svg class="swoosh" viewBox="0 0 340 40" preserveAspectRatio="none"><path d="M20 40C120 0 220 0 320 40Z" fill="url(#swooshGreen)"/><path d="M60 40C140 18 200 18 280 40Z" fill="#fff"/></svg>
</section>

<!-- Domestic services -->
<section class="page domestic-page" style="left:429px;top:411px;width:339px;height:241px;background:linear-gradient(#fff,#fafafa)">
  <h2 class="h-green" style="left:0;width:100%;text-align:center;top:20px;font-size:16.5px">Domestic Electrical Services</h2>
  <p class="copy" style="left:36px;top:44px;width:267px">Bright Harbour Electrical Limited are experts in all domestic electrical jobs. Our friendly and reliable electricians can carry out everything from full re-wiring to simply changing a light fitting. Our fully qualified electricians can personally undertake any electrical work you need and no job is too small. On top of our first class service, we offer quick response times, fair prices, and free impartial advice.</p>
  <div class="photo" role="img" aria-label="Photograph of blue network cables plugged into a patch panel" style="left:34px;top:84px;width:69px;height:45px;background:linear-gradient(135deg,#0d2f6e,#2c78c9 50%,#d8b23a)"></div>
  <h3 class="h-green" style="left:116px;top:92px;font-size:10px">Fault Finding, Repairs &amp; Re-wiring</h3>
  <p class="copy" style="left:116px;top:105px;width:190px">It is important to keep the electrics in your home in good working order. We are able to give friendly advice on the maintenance and repair of your electrical system and can also undertake both complete or partial re-wiring tasks.</p>
  <div class="photo" role="img" aria-label="Photograph of a warmly lit room with chandeliers" style="left:34px;top:147px;width:69px;height:47px;background:linear-gradient(135deg,#3a1e08,#b8741f 50%,#f0c66a)"></div>
  <h3 class="h-green" style="left:116px;top:155px;font-size:10px">INstallations and Lighting</h3>
  <p class="copy" style="left:116px;top:168px;width:190px">We have years of experience in designing and installing all different types of lighting, including LED lights. Give us a call today to arrange a free lighting consultation.</p>
  <svg class="swoosh" viewBox="0 0 340 40" preserveAspectRatio="none"><path d="M20 40C120 0 220 0 320 40Z" fill="url(#swooshGreen)"/><path d="M60 40C140 18 200 18 280 40Z" fill="#fff"/></svg>
</section>

<!-- Commercial services -->
<section class="page commercial-page" style="left:806px;top:411px;width:339px;height:241px">
  <div class="green-band" style="height:98px"></div>
  <svg style="position:absolute;left:0;top:80px;width:100%;height:20px" viewBox="0 0 340 20" preserveAspectRatio="none"><path d="M0 20V13C100 1 240 1 340 13V20Z" fill="#fff"/><path d="M0 9C100 -3 240 -3 340 9" fill="none" stroke="#fff" stroke-width="1"/></svg>
  <h2 class="band-title" style="top:11px;font-size:16.5px">Commercial Electrical Services</h2>
  <p class="copy band-copy" style="left:26px;top:33px;width:137px">Our commercial electricians are perfectly suited to carry out any type of electrical work for your business. We understand that building regulations can be tough, and are on hand to offer advice and guide you through the process. Our electricians have years of experience, and can ensure that your work is carried out on time and to budget.</p>
  <p class="copy band-copy" style="left:178px;top:33px;width:138px">If you are moving offices, Bright Harbour Electrical can advise you on the best electrical system for your business, and handle the entire process for you, from design to installation, maintenance and repairs. Each of our electricians is Kelby Traders Guild qualified, so your workplace meets all electrical health and safety standards.</p>
  <div class="photo" role="img" aria-label="Photograph of a green emergency exit sign" style="left:28px;top:112px;width:69px;height:45px;background:linear-gradient(135deg,#6b6a4a,#a9a88a 50%,#2d8f3a);border:1px solid #ccc"></div>
  <h3 class="h-green" style="left:108px;top:116px;font-size:9.5px">EMERGENCY LIGHTING</h3>
  <p class="copy" style="left:108px;top:129px;width:208px">Emergency lighting is vital for a working environment to ensure the safety of your employees. We are able to expertly install and maintain these systems, and advise you on the best solution for your business.</p>
  <div class="photo" role="img" aria-label="Photograph of a red fire alarm call point" style="left:28px;top:174px;width:69px;height:47px;background:linear-gradient(135deg,#5b0b0b,#c8241e 50%,#e9e9e9);border:1px solid #ccc"></div>
  <h3 class="h-green" style="left:108px;top:166px;font-size:9.5px">FIRE ALARM MAINTENANCE</h3>
  <p class="copy" style="left:108px;top:179px;width:208px">All fire systems must be regularly tested and maintained to prolong the life of a system and discover any faults that may occur. A system that is not maintained cannot be guaranteed to protect life and property. Regular testing keeps your fire detection and warning system compliant and fully working, carried out by a competent person alongside weekly user tests.</p>
</section>

<!-- Security & systems -->
<section class="page bokeh systems-page" style="left:197px;top:693px;width:341px;height:243px;background:linear-gradient(#fff,#fff 70%,#eee)">
  <div class="photo" role="img" aria-label="Photograph of a hand using a security alarm keypad" style="left:34px;top:21px;width:69px;height:45px;background:linear-gradient(135deg,#d9d9d9,#f2f2f2 50%,#c7a58a)"></div>
  <h3 class="h-green" style="left:116px;top:23px;font-size:10px">Security Alarms</h3>
  <p class="copy" style="left:116px;top:35px;width:192px">It's vital to keep your security system in good working order to reduce false alarms and to ensure that the alarm will be raised in the event of a break-in. A maintenance contract will ensure that your intruder alarm is inspected and tested regularly, and can often pre-empt issues with your alarm system which would otherwise require an emergency call-out.</p>
  <div class="photo" role="img" aria-label="Photograph of a bright modern office corridor with ceiling lighting" style="left:34px;top:75px;width:69px;height:45px;background:linear-gradient(135deg,#9fb4c4,#eef3f6 50%,#b7c3cc)"></div>
  <h3 class="h-green" style="left:116px;top:85px;font-size:10px">New Lighting and Power Systems</h3>
  <p class="copy" style="left:116px;top:97px;width:192px">Our commercial electricians can design and install the perfect lighting and power system for your business, and are on hand to give you advice and support that you need.</p>
  <div class="photo" role="img" aria-label="Photograph of a fingerprint biometric scanner" style="left:34px;top:140px;width:69px;height:46px;background:linear-gradient(135deg,#2a5d9a,#9cc6e8 55%,#e8f1f8)"></div>
  <h3 class="h-green" style="left:116px;top:134px;font-size:10px">Biometrics</h3>
  <p class="copy" style="left:116px;top:146px;width:192px">Unlike keys, swipe cards, proximity cards, chip and pin cards, or keypad number sequences, access through a biometric reader cannot be transferred from person to person unless explicitly authorised. It is unique, which is what makes biometric readers more secure. From major government sites to commercial buildings, biometric systems provide the ultimate in security, reliability and convenience for applications large and small.</p>
  <svg class="swoosh" viewBox="0 0 340 40" preserveAspectRatio="none"><path d="M20 40C120 0 220 0 320 40Z" fill="url(#swooshGreen)"/><path d="M60 40C140 18 200 18 280 40Z" fill="#fff"/></svg>
</section>

<!-- Electrical testing -->
<section class="page testing-page" style="left:613px;top:693px;width:340px;height:243px">
  <div class="green-band" style="height:50px"></div>
  <svg style="position:absolute;left:0;top:34px;width:100%;height:20px" viewBox="0 0 340 20" preserveAspectRatio="none"><path d="M0 20V12C100 0 240 0 340 12V20Z" fill="#fff"/><path d="M0 8C100 -3 240 -3 340 8" fill="none" stroke="#fff" stroke-width="1"/></svg>
  <h2 class="band-title" style="top:11px;font-size:15.5px;letter-spacing:.5px">ELECTRICAL TESTING</h2>
  <p class="copy" style="left:19px;top:69px;width:226px">We can carry out all electrical inspection and testing for your home or business. This is needed in order to ensure that a working or living environment is electrically safe from potential accidents. Our friendly and experienced electricians can help you, by ensuring that your employees and residents are safe from potential hazards. Not only is it vital to meet all health and safety regulations for legal reasons, but the tests will also give you complete peace of mind that your building is safe.</p>
  <p class="copy" style="left:19px;top:116px;width:226px">There are many types of Electrical Inspection, and it can often be difficult to understand exactly what level of electrical testing you need. We are on hand to guide you and provide the advice that you need.</p>
  <div class="photo" role="img" aria-label="Photograph of a yellow electrical test meter with probes" style="left:255px;top:71px;width:68px;height:54px;background:linear-gradient(135deg,#f7f7f7,#f2c21a 50%,#f7f7f7);border:1px solid #bbb"></div>
  <div class="photo" role="img" aria-label="Photograph of a yellow portable appliance tester" style="left:19px;top:165px;width:69px;height:51px;background:linear-gradient(135deg,#f7f7f7,#e6b116 50%,#333);border:1px solid #bbb"></div>
  <p class="copy" style="left:105px;top:164px;width:215px">It is important when having Electrical Inspections carried out on your property, that you employ a trustworthy and reliable company. The safety of our customers is our number one priority, which is why we always use best quality equipment in our testing process.</p>
  <p class="copy" style="left:105px;top:191px;width:215px">We also carry out Portable Appliance Testing (PAT) for businesses, landlords and individuals to ensure that the electrical products you use on a daily basis are safe. For businesses, these annual tests are mandatory by law, however we also advise that testing is carried out on personal appliances.</p>
</section>
</body>
</html>
```